KerrLow Farm

Need a nice simple clean double sided business card that has our logo and info on:
Kerr Low Farm
Martin & Felicity Kerr Low
kerrlowfarm@mailbarn.example
Martin: 1-780-555-0148
Felicity: 1-780-555-0193
Instagram @ kerrlow_farm

Contact Information for Business Card

Martin & Felicity Kerr Low kerrlowfarm@mailbarn.example Martin: 1-780-555-0148 Felicity: 1-780-555-0193

```html
<!DOCTYPE html>
<html lang="en">
<head>
<meta charset="utf-8">
<title>Kerr Low Farm – Business Card</title>
<link rel="stylesheet" href="https://fonts.googleapis.com/css2?family=Tinos&family=Montserrat:wght@500&family=Arimo&display=swap">
<style>
  :root {
    --stage: #e9e9e6;
    --leaf: #6da314;
    --leaf-dark: #5f9410;
    --leaf-light: #8dbb3e;
    --paper: #ffffff;
    --grain: #f6a71e;
    --ink: #1c1c1c;
  }
  * { box-sizing: border-box; margin: 0; padding: 0; }
  html, body { width: 1200px; height: 900px; overflow: hidden; }
  body {
    background: var(--stage);
    display: flex;
    flex-direction: column;
    align-items: center;
    justify-content: center;
    gap: 40px;
  }
  .card {
    position: relative;
    width: 640px;
    height: 366px;
    overflow: hidden;
    box-shadow: 0 6px 18px rgba(0,0,0,.18);
  }
  .card--front { background: linear-gradient(180deg, var(--leaf) 0%, var(--leaf-dark) 100%); }
  .card--back { background: var(--paper); }

  .brand {
    position: absolute;
    display: flex;
    flex-direction: column;
    align-items: center;
  }
  .brand__ring {
    width: 104px;
    height: 84px;
    border-radius: 50%;
    border: 3px solid currentColor;
    margin-bottom: 8px;
  }
  .brand__name {
    font-family: "Tinos", "Times New Roman", serif;
    font-size: 34px;
    letter-spacing: .5px;
    line-height: 1;
    white-space: nowrap;
  }
  .brand__tagline {
    font-family: "Montserrat", sans-serif;
    font-weight: 500;
    font-size: 11px;
    letter-spacing: 7px;
    margin-top: 6px;
    white-space: nowrap;
  }
  .card--front .brand { left: 120px; top: 88px; color: #fff; }
  .card--back .brand { left: 46px; top: 26px; color: var(--leaf); transform: scale(.78); transform-origin: left top; }
  .card--back .brand__tagline { color: var(--grain); }

  .wheat {
    position: absolute;
    right: 0;
    top: 0;
    width: 230px;
    height: 100%;
  }
  .card--front .wheat { background: linear-gradient(100deg, rgba(255,255,255,0) 0%, rgba(255,255,255,.18) 40%, rgba(255,255,255,.28) 100%); }
  .card--back .wheat { background: linear-gradient(160deg, rgba(246,167,30,.05) 0%, rgba(246,167,30,.35) 50%, rgba(109,163,20,.3) 100%); }

  .owners {
    position: absolute;
    left: 46px;
    top: 190px;
    font-family: "Tinos", "Times New Roman", serif;
    font-size: 28px;
    color: var(--grain);
    white-space: nowrap;
  }
  .contact {
    position: absolute;
    left: 46px;
    top: 246px;
    list-style: none;
    font-family: "Arimo", Arial, sans-serif;
    font-size: 15px;
    color: var(--ink);
    line-height: 1.35;
  }
  .contact__row { display: flex; align-items: flex-start; gap: 10px; }
  .contact__icon { width: 16px; height: 16px; flex: none; margin-top: 2px; }
  .contact__dot {
    width: 14px; height: 14px; border-radius: 50%;
    border: 2px solid var(--grain); margin: 2px 1px 0; flex: none;
  }
</style>
</head>
<body>
  <section class="card card--front" aria-label="Card front">
    <div class="brand">
      <span class="brand__ring"></span>
      <span class="brand__name">KERR LOW FARM</span>
      <span class="brand__tagline">STONE MILLED FLOUR</span>
    </div>
    <div class="wheat" role="img" aria-label="White wheat stalks illustration"></div>
  </section>

  <section class="card card--back" aria-label="Card back">
    <div class="brand">
      <span class="brand__ring"></span>
      <span class="brand__name">KERR LOW FARM</span>
      <span class="brand__tagline">STONE MILLED FLOUR</span>
    </div>
    <p class="owners">Martin &amp; Felicity Kerr Low</p>
    <ul class="contact">
      <li class="contact__row">
        <svg class="contact__icon" viewBox="0 0 24 24" aria-hidden="true"><path fill="#f6a71e" d="M6.6 10.8a15.1 15.1 0 0 0 6.6 6.6l2.2-2.2a1 1 0 0 1 1-.25 11.4 11.4 0 0 0 3.6.57 1 1 0 0 1 1 1V20a1 1 0 0 1-1 1A17 17 0 0 1 3 4a1 1 0 0 1 1-1h3.5a1 1 0 0 1 1 1c0 1.25.2 2.45.57 3.57a1 1 0 0 1-.25 1z"/></svg>
        <span>Martin: 1-780-555-0148<br>Felicity: 1-780-555-0193</span>
      </li>
      <li class="contact__row">
        <svg class="contact__icon" viewBox="0 0 24 24" aria-hidden="true"><path fill="#f6a71e" d="M2 5h20v14H2z"/><path fill="none" stroke="#fff" stroke-width="1.6" d="M2.5 5.5 12 13l9.5-7.5"/></svg>
        <span>kerrlowfarm@mailbarn.example</span>
      </li>
      <li class="contact__row">
        <span class="contact__dot" aria-hidden="true"></span>
        <span>@kerrlow_farm</span>
      </li>
    </ul>
    <div class="wheat" role="img" aria-label="Golden wheat stalks illustration"></div>
  </section>
</body>
</html>
```